We want a business card/punch card for our business. We are including examples of our current business card (we like the front of our business card and not looking to remake it). We need only back side to be designed in form of a punch card (we are including a sample of the punch card we made, but are unsatisfied). For each $180 spend (9 punches) our clients have $20 off.

Colors
886aae

```html
<!DOCTYPE html>
<html lang="en">
<head>
<meta charset="utf-8">
<title>Lumen Rituals – Business Card</title>
<link href="https://fonts.googleapis.com/css2?family=Dancing+Script:wght@500;600&family=Poppins:wght@400;500&display=swap" rel="stylesheet">
<style>
  :root {
    --bg: #9c9c9c;
    --card: #ffffff;
    --purple: #6a2c9e;
    --lilac: #886aae;
    --lilac-soft: #efe9f6;
    --logo-blue: #5a5fc4;
    --text-grey: #4a4a4a;
    --muted: #777777;
  }
  * { box-sizing: border-box; margin: 0; padding: 0; }
  html, body { width: 1200px; height: 930px; overflow: hidden; }
  body {
    background: radial-gradient(ellipse at 55% 40%, #c4c4c4 0%, var(--bg) 70%);
    font-family: "Poppins", sans-serif;
    position: relative;
  }
  .card {
    position: absolute;
    left: 250px;
    width: 700px;
    height: 400px;
    background: var(--card);
    border-radius: 28px;
    box-shadow: 0 10px 24px rgba(0,0,0,0.28);
  }
  .card--front { top: 40px; }
  .card--back { top: 490px; }

  .divider {
    position: absolute;
    width: 2px;
    background: var(--lilac);
  }
  .card--front .divider { left: 330px; top: 95px; height: 210px; }
  .card--back .divider { left: 340px; top: 44px; height: 150px; }

  /* Front: brand block */
  .brand {
    position: absolute;
    left: 50px; top: 120px;
    width: 250px;
    display: flex; flex-direction: column; align-items: center; gap: 18px;
  }
  .brand__mark {
    width: 110px; height: 110px;
    border-radius: 50%;
    background: radial-gradient(circle, #8a6bd0 0%, #b9a8e6 60%, #e6def5 100%);
  }
  .brand__name {
    font-family: "Dancing Script", cursive;
    font-weight: 600;
    font-size: 46px;
    color: var(--logo-blue);
    line-height: 1;
  }

  /* Front: services */
  .services {
    position: absolute;
    left: 380px; top: 78px;
    list-style: none;
    font-family: "Dancing Script", cursive;
    font-weight: 600;
    font-size: 31px;
    line-height: 41px;
    color: var(--purple);
  }
  .services li::before { content: "• "; font-size: 20px; vertical-align: middle; }

  /* Back: person */
  .person {
    position: absolute;
    left: 30px; width: 285px; top: 78px;
    text-align: right;
  }
  .person__name {
    font-family: "Dancing Script", cursive;
    font-weight: 500;
    font-size: 54px;
    color: var(--purple);
    line-height: 1;
  }
  .person__role {
    font-size: 14px;
    color: var(--muted);
    margin-top: 4px;
  }

  /* Back: contacts */
  .contacts {
    position: absolute;
    left: 366px; top: 42px;
    list-style: none;
    font-size: 15px;
    color: var(--text-grey);
  }
  .contacts li {
    display: flex; align-items: center; gap: 10px;
    height: 31px;
  }
  .contacts svg { width: 20px; height: 20px; flex: none; }

  /* Back: punch card */
  .punch {
    position: absolute;
    left: 40px; right: 40px; top: 222px;
    text-align: center;
  }
  .punch__title {
    font-family: "Dancing Script", cursive;
    font-weight: 600;
    font-size: 30px;
    color: var(--purple);
    line-height: 1.1;
  }
  .punch__rule {
    font-size: 13px;
    color: var(--muted);
    margin-top: 2px;
  }
  .punch__slots {
    list-style: none;
    display: flex; justify-content: center; gap: 14px;
    margin-top: 14px;
  }
  .punch__slot {
    width: 52px; height: 52px;
    border-radius: 50%;
    border: 2px dashed var(--lilac);
    display: flex; align-items: center; justify-content: center;
    font-size: 14px; font-weight: 500;
    color: var(--lilac);
  }
  .punch__slot--reward {
    border-style: solid;
    background: var(--lilac-soft);
    color: var(--purple);
    font-size: 11px;
    line-height: 1.1;
    text-align: center;
  }
</style>
</head>
<body>
  <section class="card card--front">
    <div class="brand">
      <div class="brand__mark" role="img" aria-label="Lotus emblem with meditating figure"></div>
      <div class="brand__name">Lumen Rituals</div>
    </div>
    <div class="divider"></div>
    <ul class="services">
      <li>Sexual Healing</li>
      <li>Intimacy Coaching</li>
      <li>Sound Healing</li>
      <li>Sound Baths</li>
      <li>Crystal Healing</li>
      <li>Rituals</li>
    </ul>
  </section>

  <section class="card card--back">
    <div class="person">
      <div class="person__name">Theo&amp;Lena</div>
      <div class="person__role">Director</div>
    </div>
    <div class="divider"></div>
    <ul class="contacts">
      <li>
        <svg viewBox="0 0 20 20"><circle cx="10" cy="10" r="10" fill="var(--purple)"/><path d="M7 5.5l1.6 2.2-1 1.2c.7 1.4 1.8 2.5 3.2 3.2l1.2-1 2.2 1.6-.8 1.8C9.6 14.3 5.7 10.4 5.2 6.3z" fill="#fff"/></svg>
        555-014-2290
      </li>
      <li>
        <svg viewBox="0 0 20 20"><circle cx="10" cy="10" r="10" fill="var(--purple)"/><rect x="5" y="6.5" width="10" height="7" rx="1" fill="none" stroke="#fff" stroke-width="1.3"/><path d="M5.5 7l4.5 3.5L14.5 7" fill="none" stroke="#fff" stroke-width="1.3"/></svg>
        hello@lumenrituals.com
      </li>
      <li>
        <svg viewBox="0 0 20 20"><circle cx="10" cy="10" r="10" fill="var(--purple)"/><circle cx="10" cy="10" r="5" fill="none" stroke="#fff" stroke-width="1.2"/><path d="M5 10h10M10 5c-2 2.8-2 7.2 0 10M10 5c2 2.8 2 7.2 0 10" fill="none" stroke="#fff" stroke-width="1"/></svg>
        www.lumenrituals.com
      </li>
      <li>
        <svg viewBox="0 0 20 20"><circle cx="10" cy="10" r="10" fill="var(--purple)"/><path d="M5.5 6.5h9v6h-5l-2.5 2v-2h-1.5z" fill="none" stroke="#fff" stroke-width="1.2" stroke-linejoin="round"/></svg>
        Social page: /LumenRituals
      </li>
      <li>
        <svg viewBox="0 0 20 20"><circle cx="10" cy="10" r="10" fill="var(--purple)"/><rect x="5.5" y="6.5" width="9" height="8" rx="1" fill="none" stroke="#fff" stroke-width="1.2"/><path d="M5.5 9h9M8 5.2v2.4M12 5.2v2.4" stroke="#fff" stroke-width="1.2"/></svg>
        Events page: /LumenRituals
      </li>
    </ul>

    <div class="punch">
      <div class="punch__title">Loyalty Punch Card</div>
      <div class="punch__rule">One punch for every $20 spent · 9 punches ($180) = $20 off your next session</div>
      <ol class="punch__slots">
        <li class="punch__slot">1</li>
        <li class="punch__slot">2</li>
        <li class="punch__slot">3</li>
        <li class="punch__slot">4</li>
        <li class="punch__slot">5</li>
        <li class="punch__slot">6</li>
        <li class="punch__slot">7</li>
        <li class="punch__slot">8</li>
        <li class="punch__slot punch__slot--reward">$20<br>OFF</li>
      </ol>
    </div>
  </section>
</body>
</html>
```